Lotvantage.com Webpage Design

Design Brief for lotvantage.com (Copy of Brief also in attached Word file)

Name of Website- lotvantage.com (existing logo and look & feel of website to be changed)

Logo - Finalised. The logo files are attached with the brief as “logo.jpeg”. The “Blue- Grey” version of the logo is for use on lighter backgrounds and the “Orange-White” version of the logo is for use on darker backgrounds. (A full Black version of the logo is also attached). Both versions may be used in different parts of the website. All attached files are in .png format.
Status - The website in functional and is undergoing user trials. However, we want to improve the look & feel of the website so at it seems
a. cotemporary,
b. Easy to Navigate
c. professional and
d. Vibrant.

Please visit ‘lotvantage.com’ to check out the website and its functionalities – please use it only as a reference for the features & functions to be provided, however the designer should use a ‘Free Hand’ in designing the composition of various parts of the webpage without getting too influenced by the existing design

Objective of the Website ‘lotvantage.com –
a. It is a portal focussed on listing of ‘Retail’ specific real-estate properties by developers, owners and realty brokers. The properties shall listed under the following four categories-
i. Retail Malls
ii. Shopping Complexes
iii. High-street shops
iv. Retail Warehouses
*refer lotvantage.com for better clarity

b. The abovementioned properties shall be listed either for ‘Sale’ or ‘rent\lease’ or both

c. Users shall visit the site in case they wish to acquire a retail \ shop space either on ‘sale’ or ‘rent’. These Users would be able to specify the ‘Search Criteria’ through the tool-bars provided on the website – the ‘Search Criteria’ shall comprise of ‘Type of space category’, ‘City’, ‘Locality’, transaction type ie ‘Rent \ Sale’ and ‘Area Range’

d. The main revenue model for the website shall be listing fee ( or advertising charges ) payable by those listing their properties on the website.

Three Main Pages of Website (lotvantage.com) that need to be designed -
a. Main Home Page (visit the web link - http://lotvantage.com/ ) - The main home page has the “Search Toolbar” for specifying of Search Criteria by the User. It shall also have the following features & functions-
i. Main Advertising Banner
ii. Featured Projects
iii. New Launches
iv. Toolbar with buttons – ‘Advertise with Us’, ‘Listings Alert’, ‘Lot Mavens’, ‘Advertiser Login’

b. Property Listings Page (visit the web link - http://lotvantage.com/gurgaon-in-india ) - The List of property options that match the Criteria specified by the ‘User’ get displayed on this page.

c. Property Detail Page - When the ‘User’ clicks on the “More….” Button on the ‘Property Listings Page’ (given in point b. above) the web page with the details of the property opens. (For Example – visit the web link - http://lotvantage.com/brevo-Shopping-Complex-brevo-quadrel-gurgaon-636 )

Note:- Please refer to attached ‘Shopping’ related images the designer may use them on the website to provide a look & feel of retail if required – either separately or rotate in a single window

Target Market(s)

Retailers & Investors looking for retail space, Real Estate Brokers, Developers

Industry/Entity Type

Advertising

Number of Pages Required

3 page

Requirements
Must have
• Refer to existing site lotvantage.com -- all the existing functionalities are a must have.
Nice to have
• The Designer may use the retail related images on the website if required for making it more vibrant. Refer attached images Shopping(1-6).jpg

```html
<!DOCTYPE html>
<html lang="en">
<head>
<meta charset="utf-8">
<title>Lotvantage.com – Retail Space Portal</title>
<link href="https://fonts.googleapis.com/css2?family=Oswald:wght@400;500&family=Roboto+Condensed:wght@400;700&display=swap" rel="stylesheet">
<style>
:root{
  --blue:#1a9be6;
  --blue-dark:#0f86cf;
  --ink:#222;
  --muted:#777;
  --line:#e4e4e4;
  --panel:#efefef;
  --footer:#4a4a4c;
  --footer-bottom:#3b3b3d;
  --dark-btn:#2a2a2a;
  --white:#fff;
}
*{box-sizing:border-box;margin:0;padding:0}
html,body{width:770px;height:1200px;overflow:hidden;background:var(--white)}
body{position:relative;font-family:"Roboto Condensed",sans-serif;color:var(--ink);font-size:7px}
.abs{position:absolute}
.top-rule{left:0;top:0;width:770px;height:2px;background:var(--blue)}
.util-links{right:156px;top:5px;font-size:5px;color:#555}
.util-links b{color:var(--ink)}
.brand{left:157px;top:14px;display:flex;align-items:center;gap:6px;font-size:17px;color:var(--blue);font-weight:700}
.brand .dot{width:14px;height:14px;border-radius:50%;background:var(--blue)}
.nav{left:328px;top:17px;display:flex;align-items:flex-start}
.nav .item{padding:0 12px;border-left:1px dashed #bbb;text-align:center;font-size:6.5px;text-transform:uppercase;color:var(--ink)}
.nav .item small{display:block;font-size:4.5px;color:var(--muted);text-transform:none}
.nav .home{border:0;padding:0 10px 0 0}
.city-btn{left:563px;top:19px;width:50px;height:14px;background:var(--blue);color:#fff;font-size:6.5px;display:flex;align-items:center;justify-content:center;gap:3px;border-radius:1px}
.hero{left:0;top:46px;width:770px;height:268px;background:linear-gradient(90deg,#c7a88a 0%,#e7d6c4 25%,#f1ebe2 50%,#e9c9ac 72%,#d9a48a 100%)}
.hero-rule{left:0;top:314px;width:770px;height:3px;background:var(--blue)}
.search{left:211px;top:205px;width:349px;height:96px;background:rgba(255,255,255,.88);padding:10px 12px}
.search .label{font-size:5.5px;color:#444}
.search .label a{color:var(--blue);text-decoration:none}
.check{display:flex;align-items:center;gap:5px;font-size:5.5px;color:#444}
.check i{width:7px;height:7px;border:1px solid #bbb;background:#fff;display:block}
.select{width:78px;height:11px;border:1px solid #ccc;background:#fff;font-size:5px;color:#999;padding:2px 4px;display:flex;justify-content:space-between}
.vsep{width:0;height:56px;border-left:1px dashed #bbb}
.search-btn{left:143px;top:69px;width:63px;height:19px;background:var(--blue);color:#fff;font-family:Oswald,sans-serif;font-size:11px;display:flex;align-items:center;justify-content:center}
.cat{top:336px;width:110px;text-align:center}
.cat .ico{width:52px;height:52px;border-radius:50%;background:#595959;margin:0 auto;display:flex;align-items:center;justify-content:center}
.cat h3{font-family:Oswald,sans-serif;font-weight:400;font-size:10px;margin-top:6px;text-transform:uppercase}
.cat p{font-size:7px;color:var(--muted);margin-top:2px}
.sec-head{left:156px;width:458px;display:flex;align-items:flex-end;gap:3px}
.sec-head h2{font-family:Oswald,sans-serif;font-weight:400;font-size:12px;color:var(--blue)}
.sec-head span{font-family:Oswald,sans-serif;font-size:8px;color:#444;margin-bottom:1px}
.sec-head .bar{flex:1;height:4px;background:var(--line);margin:0 0 3px 4px}
.card{width:106px;height:133px;background:#f4f4f4;box-shadow:0 1px 1px rgba(0,0,0,.12);text-align:center}
.card .city{height:18px;background:var(--blue);color:#fff;font-size:9px;line-height:18px}
.card .photo{height:57px}
.card .type{color:var(--blue);font-size:7px;margin-top:4px}
.card .name{font-size:6.5px;line-height:8px;margin:3px 6px 0}
.card .btn{display:inline-block;margin-top:5px;width:60px;height:15px;line-height:15px;background:var(--blue);color:#fff;font-size:7px}
.p1{background:linear-gradient(180deg,#7fb0d8,#a97985 60%,#6e7d8a)}
.p2{background:linear-gradient(180deg,#2d3a2c,#3f8f63 60%,#1f2a22)}
.p3{background:linear-gradient(180deg,#c9dbee,#6b6668 60%,#8e8a86)}
.p4{background:linear-gradient(180deg,#b8d2ea,#d9cdb8 60%,#a89985)}
.all-btn{left:337px;width:97px;height:24px;background:var(--dark-btn);color:#fff;font-family:Oswald,sans-serif;font-size:11px;display:flex;align-items:center;justify-content:center;border-radius:1px}
.lower{left:0;top:888px;width:770px;height:182px;background:var(--panel)}
.mavens{left:156px;top:901px;width:145px;height:154px;background:var(--blue);color:#fff;text-align:center;border-radius:2px;padding:5px 9px}
.mavens h3{font-family:Oswald,sans-serif;font-weight:400;font-size:10px;padding-bottom:4px;border-bottom:1px solid rgba(255,255,255,.4)}
.mavens p{font-size:5.2px;line-height:8px;margin-top:4px}
.field{background:var(--blue-dark);border:1px solid rgba(255,255,255,.5);height:14px;margin-top:5px;text-align:left;font-size:5.5px;padding:3px 5px;color:rgba(255,255,255,.85)}
.field.tall{height:35px}
.send{display:inline-block;margin-top:6px;width:38px;height:14px;line-height:14px;background:var(--dark-btn);font-size:6.5px}
.info{left:335px;width:279px}
.info h3{font-family:Oswald,sans-serif;font-weight:400;font-size:10px}
.info h3 em{font-style:normal;color:var(--blue)}
.info p{font-size:5.5px;line-height:8px;color:#333;margin-top:5px}
.read{display:inline-block;margin-top:6px;padding:3px 5px;background:var(--dark-btn);color:#fff;font-size:5.5px;border-radius:1px}
.footer{left:0;top:1070px;width:770px;height:114px;background:var(--footer);color:#ddd}
.footer-bottom{left:0;top:1184px;width:770px;height:16px;background:var(--footer-bottom);color:#999;font-size:4.5px;display:flex;justify-content:space-between;align-items:center;padding:0 156px 0 157px}
.f-col h4{font-size:6.5px;color:#fff;font-weight:700;margin-bottom:7px}
.f-col li{list-style:none;font-size:5px;line-height:9.6px}
.f-col li::before{content:"› ";color:#aaa}
.addr div{display:flex;gap:5px;font-size:5px;line-height:7px;margin-bottom:5px}
.addr i{width:5px;height:5px;background:#ccc;flex:none;margin-top:1px}
.social{display:flex;gap:5px;margin-top:6px}
.social span{width:8px;height:8px;border-radius:50%;background:#ddd}
.vline{width:0;height:80px;border-left:1px dashed #777}
.alert input,.alert .opt{height:11px;background:#fff;font-size:5px;color:#888;padding:2px 5px;border:0}
.alert .row{display:flex;align-items:center;gap:5px;margin-top:7px;font-size:5px}
.alert .opt{width:99px;display:flex;justify-content:space-between}
.subscribe{display:inline-block;margin-top:7px;padding:3px 6px;background:var(--blue);color:#fff;font-size:6.5px}
</style>
</head>
<body>
<div class="abs top-rule"></div>
<div class="abs util-links">List Your Property Here &nbsp; <b>ADVERTISER LOGIN / REGISTER</b></div>

<div class="abs brand"><span class="dot"></span>lotvantage.com</div>

<nav class="abs nav">
  <div class="item home"><svg width="13" height="11" viewBox="0 0 13 11"><path d="M6.5 0L0 5.5h2V11h3.5V7.5h2V11H11V5.5h2z" fill="#666"/></svg></div>
  <div class="item">Advertise with us<small>Standard listing - FREE</small></div>
  <div class="item">Lot Mavens<small>Shop Search Services</small></div>
  <div class="item">Listing Alert</div>
</nav>
<div class="abs city-btn">Select City <svg width="6" height="4" viewBox="0 0 6 4"><path d="M0 0l3 3 3-3" stroke="#fff" fill="none"/></svg></div>

<div class="abs hero" role="img" aria-label="Banner photo: smiling shopper holding colourful shopping bags in a bright mall"></div>
<div class="abs hero-rule"></div>

<form class="abs search">
  <div style="display:flex;gap:10px">
    <div style="width:125px">
      <div class="label">Select Retail Format: <a>Meaning of Retail Format</a></div>
      <div style="display:grid;grid-template-columns:1fr 1fr;gap:12px 8px;margin-top:10px">
        <div class="check"><i></i>Retail Malls</div><div class="check"><i></i>Retail Malls</div>
        <div class="check"><i></i>High Street Shops</div><div class="check"><i></i>High Street Shops</div>
      </div>
    </div>
    <div class="vsep"></div>
    <div style="width:85px">
      <div class="label">Sale Or Rent Or Both</div><div class="select" style="margin-top:3px">Select Here<span>⌄</span></div>
      <div class="label" style="margin-top:8px">Select City</div><div class="select" style="margin-top:3px">Select Here<span>⌄</span></div>
    </div>
    <div class="vsep"></div>
    <div style="width:85px">
      <div class="label">Select Locality/Micro-Market</div><div class="select" style="margin-top:3px">Select Here<span>⌄</span></div>
      <div class="label" style="margin-top:8px">Enter Keywords</div><div class="select" style="margin-top:3px">Select Here<span>⌄</span></div>
    </div>
  </div>
  <div class="abs search-btn">SEARCH</div>
</form>

<div class="abs cat" style="left:154px"><div class="ico"><svg width="26" height="20" viewBox="0 0 26 20"><path d="M2 7h22l-3 12H5z" fill="#fff"/><path d="M7 7l6-6 6 6" stroke="#fff" stroke-width="2" fill="none"/></svg></div><h3>Retail Malls</h3><p>Centrally Air-Conditioned</p></div>
<div class="abs cat" style="left:271px"><div class="ico"><svg width="26" height="20" viewBox="0 0 26 20"><rect x="2" y="1" width="10" height="18" fill="#fff"/><rect x="12" y="8" width="12" height="11" fill="#fff"/></svg></div><h3>Shopping Complex</h3><p>Non Air-Conditioned Building</p></div>
<div class="abs cat" style="left:388px"><div class="ico"><svg width="26" height="20" viewBox="0 0 26 20"><rect x="1" y="2" width="24" height="5" fill="#fff"/><rect x="3" y="9" width="20" height="10" fill="#fff"/></svg></div><h3>High Street Shops</h3><p>Road Facing Retail</p></div>
<div class="abs cat" style="left:506px"><div class="ico"><svg width="26" height="20" viewBox="0 0 26 20"><path d="M13 0L1 7v13h24V7z" fill="#fff"/></svg></div><h3>Retail Warehouses</h3><p>Back-end Ratail Storage</p></div>

<div class="abs sec-head" style="top:444px"><h2>Featured Retail Projects</h2><span>Across India</span><div class="bar"></div></div>

<div class="abs card" style="left:156px;top:475px"><div class="city">New Delhi</div><div class="photo p1" role="img" aria-label="Photo of a glass-front retail mall"></div><div class="type">Retail Malls</div><div class="name">Harbor Mall-Linden Garden Linden Garden</div><div class="btn">View the listing</div></div>
<div class="abs card" style="left:273px;top:475px"><div class="city">Faridabad</div><div class="photo p2" role="img" aria-label="Photo of a shopping complex lit at night"></div><div class="type">Shopping Complex</div><div class="name">Harbor Mall-Linden Garden Linden Garden</div><div class="btn">View the listing</div></div>
<div class="abs card" style="left:391px;top:475px"><div class="city">Gurgaon</div><div class="photo p3" role="img" aria-label="Photo of a city mall building"></div><div class="type">Retail Malls</div><div class="name">Harbor Mall-Linden Garden Linden Garden</div><div class="btn">View the listing</div></div>
<div class="abs card" style="left:508px;top:475px"><div class="city">Chennai</div><div class="photo p4" role="img" aria-label="Photo of a corner shopping complex"></div><div class="type">Shopping Complex</div><div class="name">Harbor Mall-Linden Garden Linden Garden</div><div class="btn">View the listing</div></div>

<div class="abs all-btn" style="top:624px">View All Projects</div>

<div class="abs sec-head" style="top:665px"><h2>Featured New Launches</h2><span>Across India</span><div class="bar"></div></div>

<div class="abs card" style="left:156px;top:695px"><div class="city">New Delhi</div><div class="photo p1" role="img" aria-label="Photo of a glass-front retail mall"></div><div class="type">Retail Malls</div><div class="name">Harbor Mall-Linden Garden Linden Garden</div><div class="btn">View the listing</div></div>
<div class="abs card" style="left:273px;top:695px"><div class="city">Faridabad</div><div class="photo p2" role="img" aria-label="Photo of a shopping complex lit at night"></div><div class="type">Shopping Complex</div><div class="name">Harbor Mall-Linden Garden Linden Garden</div><div class="btn">View the listing</div></div>
<div class="abs card" style="left:391px;top:695px"><div class="city">Gurgaon</div><div class="photo p3" role="img" aria-label="Photo of a city mall building"></div><div class="type">Retail Malls</div><div class="name">Harbor Mall-Linden Garden Linden Garden</div><div class="btn">View the listing</div></div>
<div class="abs card" style="left:508px;top:695px"><div class="city">Chennai</div><div class="photo p4" role="img" aria-label="Photo of a corner shopping complex"></div><div class="type">Shopping Complex</div><div class="name">Harbor Mall-Linden Garden Linden Garden</div><div class="btn">View the listing</div></div>

<div class="abs all-btn" style="top:845px">View All Projects</div>

<div class="abs lower"></div>
<div class="abs mavens">
  <h3>LOT MAVENS</h3>
  <p>Post your Retail Space requirement with us and our experts shall get back with suitable options and even help you in your transaction. This is a Free Service!</p>
  <div class="field">Enter your email address:</div>
  <div class="field" style="margin-top:6px">Mobile</div>
  <div class="field tall" style="margin-top:6px">Add Description of Requirement</div>
  <div class="send">SEND</div>
</div>

<div class="abs info" style="top:910px">
  <h3>ABOUT <em>Lotvantage.com</em></h3>
  <p>Lotvantage.com is a Specialised Web based platform for Retail Space, featuring properties across India under various formats such as Retail Malls, Shopping Complexes, High-street Shops. Also featured are ? Retail Warehouses ?</p>
  <div class="read">Read More</div>
</div>
<div class="abs info" style="top:986px">
  <h3>EDITOR'S <em>Choice</em></h3>
  <p>A "Select" Listing of Retail Properties Handpicked by our Editors based on their own positive evaluation on parameters &amp; attributes such as Design Concept, Location, Developer, Success Potential. So Read On to Check Out for yourself...</p>
  <div class="read">Read More</div>
</div>

<footer class="abs footer">
  <div class="abs f-col addr" style="left:157px;top:12px;width:110px">
    <h4>ADDRESS</h4>
    <div><i></i>Many desktop publishing packages and editors now use Lorem Ipsum.</div>
    <div><i></i>companyname@mailbox.com</div>
    <div><i></i>websiteaddressname.com</div>
    <div><i></i>000-000-0000</div>
    <div class="social"><span></span><span></span><span></span><span></span><span></span></div>
  </div>
  <div class="abs vline" style="left:268px;top:12px"></div>
  <div class="abs f-col" style="left:286px;top:12px">
    <h4>MORE LINK</h4>
    <div style="display:flex;gap:14px">
      <ul><li>There are many</li><li>Variations of passages</li><li>Lorem Ipsum</li><li>Suffered alteration</li><li>Injected humour</li><li>Randomised words</li></ul>
      <ul><li>There are many</li><li>Variations of passages</li><li>Lorem Ipsum</li><li>Suffered alteration</li><li>Injected humour</li><li>Randomised words</li></ul>
    </div>
  </div>
  <div class="abs vline" style="left:427px;top:12px"></div>
  <div class="abs f-col alert" style="left:442px;top:12px;width:172px">
    <h4>LISTING ALERT</h4>
    <div style="font-size:5px">Suscribe for Fortnightly Email update on New Listings @ Lotvantage.com</div>
    <div class="opt" style="width:172px;margin-top:5px">Email Address</div>
    <div class="row"><div class="opt">Select Option<span>⌄</span></div>(select retail format of interest)</div>
    <div class="row"><div class="opt">Select Option<span>⌄</span></div>(select cities of interest)</div>
    <div class="subscribe">Subscribe</div>
  </div>
</footer>
<div class="abs footer-bottom"><span>Copyright © 2013 Shopfloor Central.com. All rights reserved.</span><span>Designed &amp; Developed by Norwell Infotech</span></div>
</body>
</html>
```